Eye catching business card using our brand new logo
Dorvik Fabrication, Inc.
Modern
Wendell R. Fostrey
President
58 Quarry Hollow Road
Brindle, NH 03419
WFostrey@norvax.net
We would like to see many different styles of our brand new logo used in our business cards. Some would fill the card with the logo and some using it in the lower left corner of the card

```html
<!DOCTYPE html>
<html lang="en">
<head>
<meta charset="utf-8">
<title>Dorvik Fabrication, Inc. — Business Card</title>
<link rel="stylesheet" href="https://fonts.googleapis.com/css2?family=Open+Sans:wght@400;600;800&display=swap">
<style>
  :root {
    --page: #e9ebee;
    --card-white: #ffffff;
    --brand-blue: #2a2fc4;
    --brand-blue-deep: #1b1f9c;
    --brand-blue-light: #4a55e0;
    --text-dark: #3a3a3a;
    --rule: #b9bcc6;
  }
  html, body {
    margin: 0;
    width: 1200px;
    height: 1009px;
    overflow: hidden;
    background: var(--page);
    font-family: "Open Sans", Arial, sans-serif;
  }
  .sheet {
    position: relative;
    width: 1200px;
    height: 1009px;
  }
  .card {
    position: absolute;
    left: 200px;
    width: 800px;
    height: 457px;
    border-radius: 22px;
    overflow: hidden;
    box-shadow: 0 6px 18px rgba(0,0,0,0.18);
  }
  /* Front */
  .card-front { top: 31px; background: var(--card-white); }
  .front-brand {
    position: absolute;
    left: 52px;
    top: 150px;
    display: flex;
    align-items: center;
    gap: 14px;
  }
  .brand-dot {
    width: 44px;
    height: 44px;
    border-radius: 50%;
    background: var(--brand-blue);
  }
  .brand-name {
    font-weight: 800;
    font-size: 26px;
    line-height: 1.05;
    color: var(--brand-blue);
    text-transform: uppercase;
  }
  .divider {
    position: absolute;
    left: 400px;
    top: 125px;
    width: 1px;
    height: 150px;
    background: var(--rule);
  }
  .contact {
    position: absolute;
    left: 430px;
    top: 118px;
    color: var(--text-dark);
  }
  .contact-name {
    margin: 0;
    font-weight: 600;
    font-size: 24px;
    color: var(--brand-blue);
  }
  .contact-title { margin: 0 0 22px; font-size: 16px; }
  .contact-line {
    margin: 0;
    font-size: 15px;
    line-height: 22px;
    display: flex;
    align-items: center;
    gap: 8px;
  }
  .contact-line svg { width: 13px; height: 13px; fill: var(--brand-blue); }
  .contact-address { margin-bottom: 10px; }
  .front-swoosh {
    position: absolute;
    left: 0;
    bottom: 0;
    width: 800px;
    height: 160px;
  }
  /* Back */
  .card-back {
    top: 519px;
    background: radial-gradient(ellipse at 35% 30%, var(--brand-blue-light), var(--brand-blue) 55%, var(--brand-blue-deep));
  }
  .back-brand {
    position: absolute;
    right: 56px;
    bottom: 80px;
    text-align: right;
    color: var(--card-white);
    font-weight: 800;
    text-transform: uppercase;
  }
  .back-brand-main { font-size: 76px; line-height: 0.95; letter-spacing: 1px; }
  .back-brand-sub { font-size: 27px; letter-spacing: 1px; }
</style>
</head>
<body>
<main class="sheet">
  <section class="card card-front" aria-label="Business card front">
    <div class="front-brand">
      <span class="brand-dot"></span>
      <span class="brand-name">Dorvik<br>Fabrication, Inc.</span>
    </div>
    <div class="divider"></div>
    <div class="contact">
      <p class="contact-name">Wendell R. Fostrey</p>
      <p class="contact-title">President</p>
      <p class="contact-line">58 Quarry Hollow Road</p>
      <p class="contact-line contact-address">Brindle, NH 03419</p>
      <p class="contact-line">
        <svg viewBox="0 0 24 24"><path d="M6.6 10.8a15 15 0 0 0 6.6 6.6l2.2-2.2a1 1 0 0 1 1-.25 11.4 11.4 0 0 0 3.6.6 1 1 0 0 1 1 1V20a1 1 0 0 1-1 1A17 17 0 0 1 3 4a1 1 0 0 1 1-1h3.5a1 1 0 0 1 1 1c0 1.25.2 2.45.6 3.6a1 1 0 0 1-.25 1z"/></svg>
        (603) 555-0142
      </p>
      <p class="contact-line">
        <svg viewBox="0 0 24 24"><path d="M5 3h14v6H5zM3 10h18v8h-3v3H6v-3H3zm5 5v4h8v-4z"/></svg>
        (603) 555-0187
      </p>
      <p class="contact-line">
        <svg viewBox="0 0 24 24"><path d="M2 5h20v14H2zm2 2v.5l8 5 8-5V7z"/></svg>
        WFostrey@norvax.net
      </p>
    </div>
    <svg class="front-swoosh" viewBox="0 0 800 160" preserveAspectRatio="none" aria-hidden="true">
      <path d="M0 40 C 200 120, 500 140, 800 90 L800 160 L0 160 Z" fill="var(--brand-blue)"/>
      <path d="M0 40 C 220 110, 520 125, 800 70 L800 84 C 520 135, 220 122, 0 52 Z" fill="var(--brand-blue-light)" opacity="0.7"/>
      <path d="M0 22 C 240 100, 540 115, 800 55" fill="none" stroke="var(--brand-blue)" stroke-width="2"/>
      <path d="M0 75 C 250 150, 560 160, 800 120 L800 160 L0 160 Z" fill="var(--brand-blue-deep)" opacity="0.6"/>
    </svg>
  </section>

  <section class="card card-back" aria-label="Business card back">
    <div class="back-brand">
      <div class="back-brand-main">Dorvik</div>
      <div class="back-brand-sub">Fabrication, Inc.</div>
    </div>
  </section>
</main>
</body>
</html>
```